New audiology website PSD design only - guaranteed

We need a clean and attractive website to replace an existing Audiology (hearing technology) website which will be wordpress based.
The current website is: http://kvhearwell.com.au
They have a new logo and colors which you can find at www.qorvix.net/temp/kvh2018.pdf
We will no longer have a web shop in the new website
To enter the competition, we only need a sample of the home page.
The winning design will be asked to produce 2 standard page template alternatives as well (based on the winning home page design, but for a standard page layout)
The winning design must provide any photos used
We want a clean, credible site but with some warmth
Target Market(s)
All ages but needs to include the elderly
Industry/Entity Type
Medical And Science
Number of Pages Required
3 page
Look and feel
Each slider illustrates characteristics of the customer's brand and the style your logo design should communicate.

```html
<!DOCTYPE html>
<html lang="en">
<head>
<meta charset="utf-8">
<title>KV Hearwell – Home</title>
<link rel="stylesheet" href="https://fonts.googleapis.com/css2?family=Libre+Baskerville:wght@400;700&family=PT+Sans:wght@400;700&display=swap">
<style>
:root{
  --orange:#f07023;
  --orange-dark:#d95f17;
  --ink:#222;
  --muted:#666;
  --light:#fafafa;
  --footer:#333333;
  --footer-line:#4a4a4a;
  --white:#fff;
}
*{box-sizing:border-box;margin:0;padding:0}
html,body{width:1200px;height:2715px;overflow:hidden}
body{position:relative;background:var(--light);font-family:"PT Sans",Arial,sans-serif;color:var(--ink)}
.abs{position:absolute}
.serif{font-family:"Libre Baskerville",Georgia,serif}

/* hero */
.hero{left:0;top:0;width:1200px;height:690px;background:linear-gradient(120deg,#6d5a52 0%,#a58d80 30%,#c9c2bf 55%,#8e98a6 80%,#d8d6d4 100%)}
.hero-curve{left:0;top:540px;width:1200px;height:160px}
.hero-arrow{top:305px;width:34px;height:34px;background:var(--white);display:flex;align-items:center;justify-content:center}
.hero-title{left:131px;top:222px;width:620px;font-size:40px;line-height:50px;font-weight:700;color:var(--white)}
.hero-text{left:131px;top:336px;width:600px;font-size:16px;line-height:25px;font-weight:700;color:var(--white)}
.btn-outline-light{left:131px;top:414px;width:123px;height:42px;border:2px solid var(--white);color:var(--white);font-size:14px;font-weight:700;display:flex;align-items:center;justify-content:center;background:rgba(0,0,0,.25)}

/* top bar + header */
.topbar{left:0;top:0;width:1200px;height:24px;background:rgba(255,255,255,.9);border-bottom:1px solid #ddd;font-size:12px}
.topbar .social{left:130px;top:5px;display:flex;gap:10px}
.topbar .social span{width:13px;height:13px;background:#333;display:block}
.topbar .contact{right:132px;top:4px;display:flex;gap:24px;align-items:center}
.topbar .contact div{display:flex;align-items:center;gap:8px}
.header{left:0;top:24px;width:1200px;height:74px;background:rgba(255,255,255,.82)}
.brand{left:132px;top:20px;display:flex;align-items:center;gap:10px;font-family:"Libre Baskerville",Georgia,serif;font-size:25px;color:#555}
.brand i{width:30px;height:30px;border-radius:50%;background:var(--orange);display:block}
.nav{left:390px;top:30px;display:flex;gap:28px;font-size:11.5px;font-weight:700;text-transform:uppercase;color:#222}

/* about */
.about{left:132px;top:588px;width:936px;height:335px;background:var(--white);box-shadow:0 6px 10px rgba(0,0,0,.12);text-align:center}
.about h2{margin-top:52px;font-size:28px;letter-spacing:1px}
.about p{width:800px;margin:18px auto 0;font-size:12px;line-height:24px;color:var(--muted)}
.btn-orange{background:var(--orange);color:var(--white);font-weight:700;font-size:13px;display:flex;align-items:center;justify-content:center}
.about .btn-orange{width:114px;height:44px;margin:20px auto 0}

/* services + musicians */
.services{left:132px;top:997px;width:273px;height:326px;background:var(--orange);color:var(--white);padding:38px 22px}
.services h3{font-size:26px;line-height:28px}
.services p{margin-top:14px;font-size:12px;line-height:20px}
.btn-outline-white{margin-top:26px;width:96px;height:34px;border:1px solid var(--white);font-size:11px;font-weight:700;display:flex;align-items:center;justify-content:center}
.section-title{left:458px;top:993px;font-size:22px;font-weight:700}
.pager{top:998px;width:18px;height:14px;border:1px solid #bbb;background:var(--white);font-size:10px;line-height:12px;text-align:center;color:#555}
.card{top:1032px;width:279px}
.card .photo{height:145px}
.card h4{margin-top:18px;font-size:12px;line-height:20px;font-weight:700;text-transform:uppercase;padding-bottom:10px;border-bottom:1px solid #bbb}
.card p{margin-top:10px;font-size:12px;line-height:19px;color:var(--muted)}
.btn-outline-dark{margin-top:12px;width:88px;height:30px;border:1px solid #ccc;font-size:10.5px;font-weight:700;display:flex;align-items:center;justify-content:center;background:var(--white)}

/* login */
.login{left:0;top:1412px;width:1200px;height:317px;background:linear-gradient(90deg,#2a2322,#4b3f3b 50%,#2c2625);color:var(--white);text-align:center}
.login h3{margin-top:50px;font-size:24px;font-weight:700}
.login .sub{margin-top:18px;font-size:12px;font-weight:700;text-transform:uppercase}
.login .fields{margin:26px auto 0;display:flex;gap:10px;justify-content:center}
.login .fields div{width:258px;height:38px;border:1px solid #bbb;text-align:left;padding:11px 12px;font-size:12px}
.login .btn-orange{width:128px;height:38px;margin:14px auto 0;text-transform:uppercase;font-size:12px}
.login .reg{margin-top:12px;font-size:12px}

/* doctors */
.doc-photo{left:201px;top:1815px;width:398px;height:470px;background:linear-gradient(160deg,#e7e5e3,#cfcac6 50%,#3b3f4e)}
.doc-panel{left:599px;top:1815px;width:400px;height:470px;background:var(--orange);color:var(--white);padding:56px 44px}
.doc-panel h3{font-size:26px}
.doc-panel .tag{margin-top:14px;font-size:14px;font-weight:700;text-transform:uppercase}
.doc-panel p{margin-top:22px;font-size:12px;line-height:22px}
.doc-panel .btn-outline-white{width:114px;height:40px;font-size:13px}
.doc-dots{left:932px;top:2232px;display:flex;gap:6px}
.doc-dots span{width:22px;height:22px;border-radius:50%;background:var(--white);color:var(--orange);font-size:13px;line-height:22px;text-align:center;font-weight:700}

/* newsletter + footer */
.footer{left:0;top:2390px;width:1200px;height:325px;background:var(--footer);color:var(--white)}
.newsletter{left:132px;top:2357px;width:936px;height:60px;background:var(--orange);color:var(--white);display:flex;align-items:center}
.newsletter .label{width:250px;padding-left:58px;font-size:19px;font-weight:700;display:flex;align-items:center;gap:14px}
.newsletter .field{width:155px;margin-right:16px;border-bottom:1px solid rgba(255,255,255,.8);font-size:12px;padding-bottom:4px}
.newsletter .send{margin-left:auto;width:110px;height:60px;border-left:1px solid rgba(255,255,255,.6);display:flex;align-items:center;justify-content:center}
.vline{top:2470px;width:1px;height:170px;background:var(--footer-line)}
.f-brand{left:132px;top:2478px;font-family:"Libre Baskerville",Georgia,serif;font-size:25px;color:#888;display:flex;gap:10px;align-items:center}
.f-brand i{width:30px;height:30px;border-radius:50%;background:var(--orange);display:block}
.f-info{left:132px;display:flex;gap:14px;align-items:center;font-size:12px;line-height:17px}
.f-info .ic{width:30px;height:30px;border-radius:50%;background:var(--white);display:flex;align-items:center;justify-content:center}
.f-head{top:2492px;font-size:11px;font-weight:700;text-transform:uppercase}
.f-list{top:2523px;list-style:none;font-size:11.5px;line-height:24px}
.f-list li::before{content:"→ ";}
.f-social{left:986px;top:2523px;display:flex;gap:6px}
.f-social span{width:23px;height:28px;border:1px solid #aaa;background:var(--white);display:block}
.copy-line{left:0;top:2670px;width:1200px;height:1px;background:var(--footer-line)}
.copy{left:132px;top:2686px;font-size:11.5px}
.terms{right:132px;top:2686px;font-size:11.5px}
</style>
</head>
<body>

<div class="abs hero" role="img" aria-label="Audiologist fitting a hearing aid behind an elderly patient's ear"></div>
<svg class="abs hero-curve" viewBox="0 0 1200 160" preserveAspectRatio="none"><path d="M0 60 Q600 -40 1200 140 V160 H0 Z" fill="#fafafa"/></svg>
<div class="abs hero-arrow" style="left:0"><svg width="16" height="12" viewBox="0 0 16 12"><path d="M15 6H2M6 1L1 6l5 5" stroke="#f07023" stroke-width="2" fill="none"/></svg></div>
<div class="abs hero-arrow" style="right:0"><svg width="16" height="12" viewBox="0 0 16 12"><path d="M1 6h13M10 1l5 5-5 5" stroke="#f07023" stroke-width="2" fill="none"/></svg></div>
<h1 class="abs hero-title serif">KV Hearwell's Diagnostic Services</h1>
<p class="abs hero-text">KV Hearwell are state of the art hearing and balance clinics. We provide all brands of digital hearing aids, cochlear implants and assisted listening devices.</p>
<div class="abs btn-outline-light">Learn More</div>

<div class="abs topbar">
  <div class="abs social"><span></span><span></span>
    <svg width="15" height="12" viewBox="0 0 15 12"><rect x="0.5" y="0.5" width="14" height="11" fill="none" stroke="#333"/><path d="M1 1l6.5 6L14 1" fill="none" stroke="#333"/></svg></div>
  <div class="abs contact">
    <div><svg width="12" height="12" viewBox="0 0 12 12"><path d="M2 1h3l1 3-2 1a7 7 0 0 0 3 3l1-2 3 1v3c-6 1-10-3-9-9z" fill="#333"/></svg>Phone : &nbsp;9271 0488</div>
    <div><svg width="13" height="11" viewBox="0 0 13 11"><rect x="0.5" y="0.5" width="12" height="10" fill="none" stroke="#333"/><path d="M1 1l5.5 5L12 1" fill="none" stroke="#333"/></svg>Email : info@kvhearwell.com</div>
  </div>
</div>
<header class="abs header">
  <div class="abs brand"><i></i>KV Hearwell</div>
  <nav class="abs nav"><span>Your Hearing</span><span>Hearing Aids</span><span>Musicians</span><span>Doctors Information</span><span>About Us</span><span>Products</span><span>Contact Us</span></nav>
</header>

<section class="abs about">
  <h2 class="serif">ABOUT US</h2>
  <p>KV Hearwell is an independently owned and managed professional audiology clinic. Our Audiologists are health-care professionals specialising in diagnosing, treating and monitoring everything to do with hearing and balance. At KV Hearwell we work closely with Ear, Nose and Throat specialists to ensure you receive the highest standards of medical care.<br>KV Hearwell are state of the art hearing and balance clinics. We provide all brands of digital hearing aids, cochlear implants and assisted listening devices. We are diagnostic clinics, offering hearing tests for adults and children, balance tests, tinnitus testing and treatment</p>
  <div class="btn-orange">Learn More</div>
</section>

<section class="abs services">
  <h3 class="serif">KV Hearwell's Diagnostic Services</h3>
  <p>Adult Hearing Test: Pure Tone Audiometry is the standard behavioural procedure for measuring an adults sensitivity to auditory stimulus. With a series of 'pure tones' the softest level</p>
  <div class="btn-outline-white">Learn More</div>
</section>

<h2 class="abs section-title serif">Our Musicians</h2>
<div class="abs pager" style="left:1028px">←</div>
<div class="abs pager" style="left:1050px">→</div>
<article class="abs card" style="left:458px">
  <div class="photo" role="img" aria-label="Clear custom in-ear monitors on a grey surface" style="background:linear-gradient(135deg,#9a9a9a,#5e5e5e 50%,#b5b5b5)"></div>
  <h4>KV Hearwell are resellers for Torrin Audio and Bellwave</h4>
  <p>Our Audiologists can take professional ear impressions for your custom fit In Ear Monitors.</p>
  <div class="btn-outline-dark">LEARN MORE</div>
</article>
<article class="abs card" style="left:787px">
  <div class="photo" role="img" aria-label="Blue custom in-ear monitors on a white background" style="background:linear-gradient(135deg,#e6e9ee,#3f63b8 45%,#2a4f9e 60%,#e9ecef)"></div>
  <h4>KV Hearwell are resellers for Torrin Audio and Bellwave</h4>
  <p>Our Audiologists can take professional ear impressions for your custom fit In Ear Monitors.</p>
  <div class="btn-outline-dark">LEARN MORE</div>
</article>

<section class="abs login" role="img" aria-label="Dark background photograph of a clinic consultation">
  <h3 class="serif">Login</h3>
  <div class="sub">If you already have an account with us, please login here</div>
  <div class="fields"><div>UserName or E-mail</div><div>Password</div></div>
  <div class="btn-orange">Submit</div>
  <div class="reg">Not registered ?</div>
</section>

<div class="abs doc-photo" role="img" aria-label="Audiologist placing test electrodes on a reclining patient"></div>
<section class="abs doc-panel">
  <h3 class="serif">Doctores Information</h3>
  <div class="tag">KV Hearwell</div>
  <p>Hearing aids in the bronze level jump in technology, adding adaptive directional microphones which allows for the reduction of dominant background noise even from a source which is moving. An increase in programmable channels gives a greater flexibility to tailor to an individuals hearing loss. Consequently the sound quality takes on a more natural sound. With each increase in technology level we see further improvements in this area and an increase in flexibility and therefore an improvement</p>
  <div class="btn-outline-white">Learn More</div>
</section>
<div class="abs doc-dots"><span>‹</span><span>›</span></div>

<footer class="abs footer"></footer>
<div class="abs newsletter">
  <div class="label serif">Our Newsletter
    <svg width="26" height="18" viewBox="0 0 26 18"><rect x="1" y="1" width="24" height="16" fill="none" stroke="#fff" stroke-width="1.5"/><path d="M1 1l12 9 12-9" fill="none" stroke="#fff" stroke-width="1.5"/></svg></div>
  <div class="field">First Name</div><div class="field">Last Name</div><div class="field">E-mail</div>
  <div class="send"><svg width="22" height="18" viewBox="0 0 22 18"><path d="M13 1l8 7-8 7V11C7 11 3 13 1 17 1 10 5 5 13 5z" fill="#fff"/></svg></div>
</div>

<div class="abs vline" style="left:389px"></div>
<div class="abs vline" style="left:568px"></div>
<div class="abs vline" style="left:930px"></div>
<div class="abs f-brand"><i></i>KV Hearwell</div>
<div class="abs f-info" style="top:2541px"><span class="ic"><svg width="14" height="14" viewBox="0 0 14 14"><path d="M7 1L1 7h2v6h3V9h2v4h3V7h2z" fill="#f07023"/></svg></span>Ground Floor, Suite 4, 120 Harbour<br>Road, Lindfield, NSW, 2070</div>
<div class="abs f-info" style="top:2597px"><span class="ic"><svg width="14" height="14" viewBox="0 0 12 12"><path d="M2 1h3l1 3-2 1a7 7 0 0 0 3 3l1-2 3 1v3c-6 1-10-3-9-9z" fill="#f07023"/></svg></span>Phone: 9271 0488</div>

<div class="abs f-head" style="left:438px">Quick Links</div>
<ul class="abs f-list" style="left:438px"><li>Site Map</li><li>Support</li><li>Help</li><li>Privacy Policy</li></ul>
<div class="abs f-head" style="left:615px">Navigation</div>
<ul class="abs f-list" style="left:615px"><li>Your Hearing</li><li>Hearing Aids</li><li>Musicians</li><li>Doctors Information</li></ul>
<ul class="abs f-list" style="left:804px"><li>About Us</li><li>Products</li><li>Contact Us</li><li>Search</li></ul>
<div class="abs f-head" style="left:986px">Follow Us</div>
<div class="abs f-social"><span></span><span></span>
  <svg width="23" height="28" viewBox="0 0 23 28"><rect x="0.5" y="0.5" width="22" height="27" fill="#333" stroke="#aaa"/><rect x="5" y="9" width="13" height="10" fill="none" stroke="#fff"/><path d="M5 9l6.5 6L18 9" fill="none" stroke="#fff"/></svg></div>

<div class="abs copy-line"></div>
<div class="abs copy">Copyright 2018 © kvhearwell All Rights Reserved.</div>
<div class="abs terms">Terms and Conditions</div>

</body>
</html>
```